We are an appraisal and dispute resolution company that works with insurance companies and insureds.

We need a website built that appeals to insurance companies as well as insureds to entrust we can assist come to a resolution with their property insurance claim.

Target Market(s)

Insurance Carriers and Insureds

Industry/Entity Type

Insurance

Coding

Coded - Design and coding required

Number of Pages Required

5+ page

Requirements
Must have
• Would like to click on pages and it take you down one page to that specific section
Nice to have
• Clean look

```html
<!DOCTYPE html>
<html lang="en">
<head>
<meta charset="utf-8">
<title>Arbita — Appraisal &amp; Claim Resolution</title>
<link href="https://fonts.googleapis.com/css2?family=Roboto:wght@300;400;500;700;900&display=swap" rel="stylesheet">
<style>
:root{
  --teal:#2fb7b6;
  --teal-dark:#239e9d;
  --ink:#1d2029;
  --text:#2a2d34;
  --muted:#5b5f66;
  --line:#c9cccf;
  --night:#1c1f27;
  --white:#ffffff;
}
*{margin:0;padding:0;box-sizing:border-box}
html,body{width:1200px;height:4666px;overflow:hidden}
body{font-family:'Roboto',Arial,sans-serif;color:var(--text);background:var(--white);position:relative}
.abs{position:absolute}
.photo{position:absolute}

/* hero */
.hero{position:absolute;left:0;top:0;width:1200px;height:706px;background:linear-gradient(135deg,#3e3a33 0%,#7a6a55 35%,#b79a78 55%,#8a7560 75%,#3a3a35 100%)}
.hero-shade{position:absolute;inset:0;background:linear-gradient(180deg,rgba(20,22,26,.55) 0%,rgba(20,22,26,.25) 45%,rgba(20,22,26,.15) 100%)}
.nav a{position:absolute;top:42px;color:var(--white);font-size:14px;font-weight:500;text-decoration:none}
.brand{position:absolute;left:480px;top:18px;width:200px;text-align:center;color:var(--white)}
.brand-name{font-size:40px;font-weight:700;letter-spacing:2px;line-height:44px}
.brand-tag{font-size:7px;font-weight:700;letter-spacing:.5px;line-height:10px}
.btn-start{position:absolute;left:948px;top:22px;width:150px;height:43px;background:var(--teal);color:var(--white);font-size:16px;font-weight:700;display:flex;align-items:center;justify-content:center;box-shadow:3px 3px 0 rgba(255,255,255,.5)}
.hero-frame{position:absolute;left:382px;top:100px;width:436px;height:262px;border:2px solid var(--white);border-bottom:none}
.hero-frame-cut{position:absolute;left:382px;top:362px;width:436px;height:0}
.hero-kicker{position:absolute;left:382px;top:138px;width:436px;text-align:center;color:var(--teal);font-size:15px;font-weight:500}
.hero-title{position:absolute;left:150px;top:178px;width:900px;text-align:center;color:var(--white);font-size:46px;font-weight:700;line-height:63px;background:transparent}
.hero-title span{background:transparent}
.social-rail{position:absolute;left:1142px;top:178px;width:32px}
.social-rail .dot{width:32px;height:32px;border:1.5px solid var(--white);border-radius:50%;margin-bottom:10px}
.social-rail .sq{width:10px;height:10px;background:var(--white);margin:0 auto 28px}
.scroll{position:absolute;left:1150px;top:420px;width:16px;height:130px}
.scroll-text{position:absolute;left:1084px;top:462px;transform:rotate(-90deg);color:var(--white);font-size:10px;letter-spacing:1px;width:100px;text-align:center}
.down-wrap{position:absolute;left:549px;top:656px;width:100px;height:100px;border-radius:50%;background:var(--white);border:2px solid #d4d6d8}
.down-inner{position:absolute;left:12px;top:12px;width:72px;height:72px;border-radius:50%;background:var(--white);box-shadow:0 2px 10px rgba(0,0,0,.15);display:flex;align-items:center;justify-content:center}

/* common */
.eyebrow{font-size:15px;font-weight:700;letter-spacing:2px;color:var(--ink)}
.eyebrow.bar{padding-left:14px;border-left:6px solid var(--teal);line-height:22px}
.eyebrow.teal{color:var(--teal)}
.display{font-size:35px;font-weight:400;line-height:53px;color:var(--ink)}
.display b{font-weight:700}
.body-copy{font-size:13.5px;line-height:30px;color:var(--muted)}
.link-btn{position:absolute;height:42px;display:flex;align-items:center;padding-left:18px;font-size:15px;font-weight:700;color:var(--ink);border-left:2px solid var(--teal);border-top:2px solid var(--teal);border-bottom:2px solid var(--teal)}
.link-btn::after{content:"";position:absolute;right:0;top:-2px;height:2px}
.link-btn svg{margin-left:8px}

/* mission */
.mission-frame{position:absolute;left:112px;top:1108px;width:670px;height:235px;border:3px solid var(--teal);border-right:none;border-bottom:none}
.mission-frame-side{position:absolute;left:112px;top:1108px;width:3px;height:235px;background:var(--teal)}
.mission-copy{position:absolute;left:143px;top:1513px;padding-left:24px;border-left:5px solid var(--teal);width:460px}
.mission-copy h4{font-size:16px;font-weight:700;color:var(--ink);line-height:26px;margin-top:0}
.mission-copy p{font-size:13px;line-height:30px;color:var(--muted)}

/* cards */
.card{position:absolute;top:1931px;width:297px;height:230px;border:2px solid var(--line);border-top:none}
.card::before,.card::after{content:"";position:absolute;top:0;height:2px;background:var(--line)}
.card::before{left:-2px;width:90px}
.card::after{right:-2px;width:90px}
.card-icon{position:absolute;left:86px;top:-54px;width:123px;height:112px;border:2px solid var(--ink);background:var(--white);padding:7px}
.card-icon div{width:100%;height:100%;background:var(--teal)}
.card h3{position:absolute;top:76px;left:0;width:100%;text-align:center;font-size:26px;font-weight:700;color:var(--ink)}
.card p{position:absolute;top:118px;left:18px;right:18px;text-align:center;font-size:13px;line-height:30px;color:var(--muted)}

/* news */
.news-small .img{position:absolute;width:233px;height:174px}
.news-date{font-size:14px;color:var(--ink);font-weight:500}
.news-title{font-size:16px;font-weight:700;color:var(--ink);line-height:27px}

/* contact */
.night{position:absolute;left:0;top:3957px;width:1200px;height:709px;background:var(--night)}
.contact-teal{position:absolute;left:112px;top:3774px;width:455px;height:346px;background:var(--teal)}
.contact-outline{position:absolute;left:719px;top:3825px;width:367px;height:307px;border:2px solid var(--teal)}
.form-card{position:absolute;left:393px;top:3861px;width:660px;height:443px;background:var(--white);box-shadow:0 6px 24px rgba(0,0,0,.12)}
.field{position:absolute;width:268px}
.field label{display:block;font-size:11px;font-weight:700;color:var(--ink);letter-spacing:.3px}
.field span{display:block;margin-top:22px;font-size:12.5px;color:#a5a8ac;padding-bottom:8px;border-bottom:1px solid var(--line)}

/* footer */
.foot-h{font-size:15px;font-weight:700;color:var(--white);letter-spacing:.5px}
.foot-list{list-style:none;margin-top:26px}
.foot-list li{font-size:14px;color:#d7d9dc;line-height:30.5px}
.foot-social{position:absolute;top:4463px;width:36px;height:36px;border:1.5px solid var(--teal)}
.contact-list{list-style:none;margin-top:26px}
.contact-list li{display:flex;font-size:14px;color:#d7d9dc;line-height:30.5px}
.contact-list svg{flex:0 0 auto;margin:9px 12px 0 0}
.foot-rule{position:absolute;left:70px;top:4590px;width:1130px;height:1px;background:#4a4e57}
.foot-bottom{position:absolute;top:4602px;font-size:12px;color:#d7d9dc}
</style>
</head>
<body>

<!-- HERO -->
<header class="hero">
  <div class="photo" role="img" aria-label="Photo of a smiling couple reviewing documents with an advisor holding a small house model" style="inset:0;background:linear-gradient(120deg,#4a4036 0%,#8c7862 30%,#c4a585 50%,#9c8a76 70%,#4d4b44 100%)"></div>
  <div class="hero-shade"></div>
  <nav class="nav">
    <a href="#top" style="left:114px">Home</a>
    <a href="#about" style="left:191px">About Us</a>
    <a href="#services" style="left:291px">What We Do</a>
    <a href="#news" style="left:764px">Blogs</a>
    <a href="#contact" style="left:839px">Contact Us</a>
  </nav>
  <div class="brand">
    <div class="brand-name">ARBITA</div>
    <div class="brand-tag">ARBITA APPRAISAL &amp; CLAIM RESOLUTION</div>
  </div>
  <a class="btn-start">Get Started</a>
  <div class="hero-frame"></div>
  <div class="abs" style="left:382px;top:362px;width:2px;height:0"></div>
  <div class="hero-kicker">LOREM IPSUM DOLOR SIT AMET, CONSECTETUR</div>
  <h1 class="hero-title">LOREM IPSUM DOLOR SIT AMET<br>CONSECTETUR ADIPISCING</h1>
  <div class="abs" style="left:382px;top:310px;width:2px;height:52px;background:var(--white)"></div>
  <div class="abs" style="left:816px;top:310px;width:2px;height:52px;background:var(--white)"></div>
  <div class="hero-frame" style="height:210px"></div>
  <div class="abs" style="left:384px;top:310px;width:432px;height:60px;background:transparent"></div>

  <div class="social-rail">
    <div class="dot"></div>
    <div class="sq"></div>
    <div class="sq"></div>
    <div class="sq"></div>
  </div>
  <div class="abs" style="left:1157px;top:330px;width:2px;height:68px;background:rgba(255,255,255,.7)"></div>
  <div class="scroll-text">SCROLL DOWN</div>
  <div class="abs" style="left:1158px;top:420px;width:1px;height:100px;background:rgba(255,255,255,.7)"></div>
  <div class="abs" style="left:1149px;top:520px;width:18px;height:18px;border-radius:50%;background:var(--teal)"></div>
  <svg class="abs" style="left:1152px;top:538px" width="12" height="14" viewBox="0 0 12 14"><path d="M6 0v12M2 8l4 4 4-4" stroke="#fff" stroke-width="1.5" fill="none"/></svg>
</header>
<div class="down-wrap"><div class="down-inner">
  <svg width="16" height="26" viewBox="0 0 16 26"><path d="M8 1v22M2 17l6 6 6-6" stroke="#2fb7b6" stroke-width="2.5" fill="none"/></svg>
</div></div>

<!-- ABOUT -->
<section id="about">
  <div class="abs eyebrow bar" style="left:112px;top:812px">ABOUT ARBITA</div>
  <h2 class="abs display" style="left:112px;top:846px;width:450px">Lorem ipsum dolor sit amet consectetur <b>adipiscing elit sed do eiusmod</b> tempor.</h2>
  <p class="abs body-copy" style="left:599px;top:808px;width:500px">Lorem ipsum dolor sit amet, consectetur adipiscing elit, sed do eiusmod tempor incididunt ut labore et<br>dolore magna aliqua. Ut enim ad minim veniam, quis nostrud exercitation ullamco laboris nisi ut aliquip ex ea commodo consequat. Duis aute irure dolor in reprehenderit in voluptate velit esse cillum dolore eu fugiat nulla pariatur. Excepteur sint occaecat cupidata.</p>
  <a class="link-btn" style="left:599px;top:1008px;width:200px">Learn More About ARBITA
    <svg width="18" height="10" viewBox="0 0 18 10"><path d="M0 5h16M12 1l4 4-4 4" stroke="#2fb7b6" stroke-width="2" fill="none"/></svg></a>

  <div class="mission-frame"></div>
  <div class="abs" style="left:112px;top:1108px;width:3px;height:235px;background:var(--teal)"></div>
  <div class="photo" role="img" aria-label="Photo of a businessman holding an umbrella above a city skyline under a bright sky" style="left:138px;top:1133px;width:756px;height:357px;background:linear-gradient(160deg,#cfdbe6 0%,#9fb4c6 40%,#6e8296 70%,#3f4b58 100%)"></div>
  <div class="photo" role="img" aria-label="Photo of a senior couple meeting an advisor at a table with a laptop" style="left:686px;top:1309px;width:404px;height:320px;background:linear-gradient(135deg,#dfe3e6 0%,#a8b3bd 40%,#6f7c88 75%,#3a4550 100%);box-shadow:0 8px 24px rgba(0,0,0,.2)"></div>
  <div class="mission-copy">
    <h4>OUR MISSION</h4>
    <p>Lorem ipsum dolor sit amet, consectetur adipiscing elit, sed do eiusmod tempor incididunt ut labore et dolore magna aliqua. Quis ipsum suspendisse ultrices gravida.</p>
  </div>

  <div class="abs eyebrow teal" style="left:0;top:1718px;width:1200px;text-align:center">ABOUT ARBITA</div>
  <h2 class="abs display" style="left:200px;top:1742px;width:800px;text-align:center">Lorem ipsum dolor sit ametconsectetur <b>adipiscing elit sed do eiusmod</b> tempor.</h2>

  <div class="card" style="left:112px">
    <div class="card-icon"><div role="img" aria-label="Icon of a checklist clipboard with a shield"></div></div>
    <h3>Lorem ipsum dolor sit</h3>
    <p>Lorem ipsum dolor sit amet, consecte-tur adipiscing elit, sed do eiusmod tempor incididunt ut labore et.</p>
  </div>
  <div class="card" style="left:451px">
    <div class="card-icon"><div role="img" aria-label="Icon of an umbrella over money and a house"></div></div>
    <h3>Lorem ipsum dolor sit</h3>
    <p>Lorem ipsum dolor sit amet, consecte-tur adipiscing elit, sed do eiusmod tempor incididunt ut labore et.</p>
  </div>
  <div class="card" style="left:791px">
    <div class="card-icon"><div role="img" aria-label="Icon of a policy document with a shield"></div></div>
    <h3>Lorem ipsum dolor sit</h3>
    <p>Lorem ipsum dolor sit amet, consecte-tur adipiscing elit, sed do eiusmod tempor incididunt ut labore et.</p>
  </div>
</section>

<!-- WHAT WE DO -->
<section id="services">
  <div class="abs eyebrow bar" style="left:112px;top:2302px">WHAT WE DO</div>
  <h2 class="abs display" style="left:112px;top:2336px;width:450px">Lorem ipsum dolor sit amet consectetur <b>adipiscing elit sed do eiusmod</b> tempor.</h2>
  <p class="abs body-copy" style="left:112px;top:2499px;width:460px">Lorem ipsum dolor sit amet, consectetur adipiscing elit, sed do eius-mod tempor incididunt ut labore et dolore magna aliqua. Quis ipsum suspendisse ultrices gravida. Risus commodo viverra maecenas ac-cumsan lacus vel facilisis. sed ut perspiciatis unde omnis iste natus error sit voluptatem accusantium doloremque laudantium, totam rem aperiam, eaque ipsa quae ab illo inventore veritatis et quasi architec-to beatae vitae dicta sunt explicabo. Nemo enim ipsam voluptatem quia voluptas sit aspernatur aut odit aut fugit, sed quia consequuntur magni dolores eos qui ratione voluptatem sequi nesciunt.</p>
  <a class="link-btn" style="left:112px;top:2787px;width:226px">Learn More What We Do
    <svg width="18" height="10" viewBox="0 0 18 10"><path d="M0 5h16M12 1l4 4-4 4" stroke="#2fb7b6" stroke-width="2" fill="none"/></svg></a>
  <div class="abs" style="left:599px;top:2244px;width:2px;height:594px;background:var(--teal)"></div>
  <div class="abs" style="left:599px;top:2836px;width:601px;height:2px;background:var(--teal)"></div>
  <div class="photo" role="img" aria-label="Photo of a smiling couple with coffee meeting an advisor in a bright office" style="left:626px;top:2266px;width:574px;height:554px;background:linear-gradient(120deg,#f1dcb3 0%,#d3b084 30%,#9c7a58 60%,#4e3d30 100%)"></div>
</section>

<!-- NEWS -->
<section id="news">
  <div class="abs eyebrow teal" style="left:0;top:2920px;width:1200px;text-align:center">NEWS AND BLOGS</div>
  <h2 class="abs" style="left:0;top:2950px;width:1200px;text-align:center;font-size:36px;font-weight:400;color:var(--ink)"><b>Latest</b> News <b>And</b> Blogs</h2>

  <div class="photo" role="img" aria-label="Photo of two businessmen in conversation" style="left:112px;top:3017px;width:476px;height:567px;background:linear-gradient(100deg,#1f2226 0%,#3a3e44 45%,#7d8690 80%,#b6bec6 100%)"></div>
  <div class="abs" style="left:112px;top:3300px;width:476px;height:284px;background:linear-gradient(180deg,rgba(0,0,0,0) 0%,rgba(0,0,0,.7) 100%)"></div>
  <div class="abs" style="left:143px;top:3412px;width:420px;color:var(--white)">
    <div style="font-size:16px">14 july 2021</div>
    <div style="font-size:20px;font-weight:700;line-height:35px;margin-top:14px">Lorem ipsum dolor sit amet, consectetur adipiscing elit sed do eiusmod.</div>
    <div style="font-size:13px;margin-top:16px">Sed ut perspiciatis unde omnis iste natus error sit</div>
  </div>

  <div class="photo" role="img" aria-label="Photo of a couple reviewing papers at home" style="left:605px;top:3017px;width:233px;height:174px;background:linear-gradient(135deg,#c8c3b7,#7f7a6c 60%,#4a473f)"></div>
  <div class="photo" role="img" aria-label="Photo of a senior couple talking with an advisor" style="left:856px;top:3017px;width:234px;height:174px;background:linear-gradient(135deg,#dcdedf,#9ea4a8 55%,#5d6468)"></div>
  <div class="photo" role="img" aria-label="Photo of a couple signing documents with an agent" style="left:605px;top:3312px;width:233px;height:174px;background:linear-gradient(135deg,#e8e6e2,#aaa39a 55%,#5b544c)"></div>
  <div class="photo" role="img" aria-label="Photo of a family meeting an advisor at a desk" style="left:856px;top:3312px;width:234px;height:174px;background:linear-gradient(135deg,#e6dcd6,#b39e96 55%,#6e5a56)"></div>

  <div class="abs" style="left:605px;top:3198px;width:233px">
    <div class="news-date">14 july 2021</div>
    <div class="news-title" style="margin-top:4px">Lorem ipsum dolor sit ametco nsectetur adipiscing elit.</div>
  </div>
  <div class="abs" style="left:856px;top:3198px;width:234px">
    <div class="news-date">14 july 2021</div>
    <div class="news-title" style="margin-top:4px">Lorem ipsum dolor sit ametco nsectetur adipiscing elit.</div>
  </div>
  <div class="abs" style="left:605px;top:3493px;width:233px">
    <div class="news-date">14 july 2021</div>
    <div class="news-title" style="margin-top:4px">Lorem ipsum dolor sit ametco nsectetur adipiscing elit.</div>
  </div>
  <div class="abs" style="left:856px;top:3493px;width:234px">
    <div class="news-date">14 july 2021</div>
    <div class="news-title" style="margin-top:4px">Lorem ipsum dolor sit ametco nsectetur adipiscing elit.</div>
  </div>
  <div class="abs" style="left:478px;top:3645px;width:243px;height:44px;border:2px solid var(--ink)"></div>
  <div class="abs" style="left:478px;top:3634px;width:237px;height:44px;background:var(--teal);color:var(--white);font-size:16px;font-weight:700;display:flex;align-items:center;justify-content:center">View More News &amp; Blogs</div>
</section>

<!-- CONTACT -->
<section id="contact">
  <div class="night"></div>
  <div class="contact-teal"></div>
  <div class="contact-outline"></div>
  <div class="abs" style="left:112px;top:3862px;width:250px;text-align:right;color:var(--white);font-size:15px;font-weight:500">CONTACT US</div>
  <div class="abs" style="left:112px;top:3888px;width:260px;text-align:right;color:var(--white);font-size:42px;font-weight:500;line-height:56px">Lorem ipsum dolor sit ame consectetur</div>
  <div class="form-card">
    <div class="abs" style="left:42px;top:42px;font-size:28px;font-weight:700;color:var(--ink)">Send Us A Message</div>
    <div class="field" style="left:45px;top:106px"><label>YOUR NAME</label><span>John Smith</span></div>
    <div class="field" style="left:340px;top:106px"><label>COMPANY</label><span>johnsmith@example.com</span></div>
    <div class="field" style="left:45px;top:207px"><label>EMAIL ADDRESS</label><span>johnsmith@example.com</span></div>
    <div class="field" style="left:340px;top:207px"><label>PHONE NUMBER</label><span>123 456 7890</span></div>
    <div class="field" style="left:53px;top:310px;width:510px"><label>MESSAGE</label><span>Sed ut perspiciatis unde omnis iste natus error sit voluptatem</span></div>
    <div class="abs" style="left:554px;top:332px;width:62px;height:62px;border-radius:50%;background:var(--teal);display:flex;align-items:center;justify-content:center">
      <svg width="26" height="26" viewBox="0 0 24 24"><path d="M22 2L2 10l8 3 3 8z" fill="#fff"/><path d="M22 2L10 13" stroke="#2fb7b6" stroke-width="1.5"/></svg>
    </div>
  </div>
</section>

<!-- FOOTER -->
<footer>
  <div class="abs" style="left:103px;top:4364px;width:205px;color:var(--white)">
    <div style="font-size:46px;font-weight:700;letter-spacing:2px;line-height:50px">ARBITA</div>
    <div style="font-size:7.5px;font-weight:700;letter-spacing:.4px;margin-top:2px">ARBITA APPRAISAL &amp; CLAIM RESOLUTION</div>
  </div>
  <div class="foot-social" style="left:109px"></div>
  <div class="foot-social" style="left:160px"></div>
  <div class="foot-social" style="left:212px"></div>
  <div class="foot-social" style="left:264px"></div>

  <div class="abs" style="left:387px;top:4358px">
    <div class="foot-h">QUICK LINKS</div>
    <ul class="foot-list"><li>Home</li><li>About Us</li><li>What We Do</li><li>Blogs</li><li>Contact US</li></ul>
  </div>
  <div class="abs" style="left:594px;top:4358px">
    <div class="foot-h">OUR SERVICES</div>
    <ul class="foot-list"><li>Sed ut perspiciatis</li><li>Unde omnis iste natus</li><li>Error sit voluptatem</li><li>Accusantium doloremque</li><li>Laudantium</li></ul>
  </div>
  <div class="abs" style="left:860px;top:4358px;width:260px">
    <div class="foot-h">CONTACT US</div>
    <ul class="contact-list">
      <li><svg width="12" height="16" viewBox="0 0 12 16"><path d="M6 0a6 6 0 0 0-6 6c0 4.5 6 10 6 10s6-5.5 6-10a6 6 0 0 0-6-6zm0 8.5A2.5 2.5 0 1 1 6 3.5a2.5 2.5 0 0 1 0 5z" fill="#2fb7b6"/></svg><span>123 Lorem ipsum dolor sit amet consectetur adipiscing elit.</span></li>
      <li style="margin-top:6px"><svg width="13" height="13" viewBox="0 0 24 24"><path d="M6.6 10.8a15 15 0 0 0 6.6 6.6l2.2-2.2c.3-.3.7-.4 1-.2 1.1.4 2.3.6 3.6.6.6 0 1 .4 1 1V20c0 .6-.4 1-1 1A17 17 0 0 1 3 4c0-.6.4-1 1-1h3.5c.6 0 1 .4 1 1 0 1.3.2 2.5.6 3.6.1.3 0 .7-.2 1z" fill="#2fb7b6"/></svg><span>123 456 7890</span></li>
      <li style="margin-top:10px"><svg width="14" height="11" viewBox="0 0 14 11"><rect width="14" height="11" fill="#2fb7b6"/><path d="M0 0l7 6 7-6" stroke="#1c1f27" stroke-width="1.3" fill="none"/></svg><span>info@arbita-mail.com</span></li>
    </ul>
  </div>
  <div class="foot-rule"></div>
  <div class="foot-bottom" style="left:89px">© copyrights 2021 ARBITA &nbsp;|&nbsp;&nbsp;&nbsp;&nbsp; All rights reserved.</div>
  <div class="foot-bottom" style="left:888px">Privacy Policy &nbsp;|&nbsp;&nbsp;&nbsp; Terms &amp; Conditions</div>
  <div class="foot-bottom" style="left:1152px">C 43</div>
</footer>

</body>
</html>
```